Facebook Post for Fence Spring Sale

We have a $12 / FT Fence sale that we have been running for a while now. We need a flyer made up for SPRING.

Our previous flyer can be seen here:
https://media.pixvault-host.example/img/48213907_551903288146720_7391026458813302947_n.jpg?ref=7c21b9e04d8a

We want to use the photos that are shown here https://files.cloudtrove-share.example/view?id=9XkQ7rTmw2LpZdVa4HsE in the flyer. This is to be posted on Facebook so it must be the proper size for Facebook page post.

The wording to be used should be "Spring Fence Sale" and "$12 / FT Wood Fences" Also we should include our business name "Oakridge Fence" and phone number for Free Estimates - 555-314-2076.

Residential Construction

Font styles to use
Serif
Sans Serif

Colors
3176b5
fbee3d
fbed22
fbf289
85cae6
33a6d7

Requirements
Must have
• Phone number, $12 / FT Fence Sale

```html
<!DOCTYPE html>
<html lang="en">
<head>
<meta charset="utf-8">
<title>Oakridge Fence – Spring Fence Sale</title>
<link rel="stylesheet" href="https://fonts.googleapis.com/css2?family=Playfair+Display:ital,wght@1,800&family=Roboto:ital,wght@0,400;0,700;0,900;1,400&family=Alfa+Slab+One&display=swap">
<style>
  :root {
    --stage: #e9e6e1;
    --wood-light: #b07a45;
    --wood-mid: #7a4a24;
    --wood-dark: #3a2011;
    --yellow: #fbee3d;
    --yellow-deep: #fbed22;
    --yellow-soft: #fbf289;
    --olive: #c9c065;
    --blue: #3176b5;
    --sky: #85cae6;
    --white: #ffffff;
    --paper: #f4f4f2;
    --brown-text: #7b4a22;
    --ink: #222222;
  }
  * { margin: 0; padding: 0; box-sizing: border-box; }
  html, body { width: 1200px; height: 1000px; overflow: hidden; background: var(--stage); }
  .post {
    position: absolute; left: 205px; top: 105px; width: 790px; height: 790px;
    overflow: hidden; font-family: "Roboto", Arial, sans-serif;
  }
  .post__shapes { position: absolute; inset: 0; }
  .brand {
    position: absolute; left: 552px; top: 0; width: 198px; height: 84px;
    display: flex; align-items: center; justify-content: center; gap: 9px;
  }
  .brand__mark { width: 22px; height: 22px; background: var(--brown-text); }
  .brand__name { font-size: 17px; font-weight: 700; color: var(--blue); }
  .headline__spring {
    position: absolute; left: 78px; top: 20px;
    font-family: "Playfair Display", Georgia, serif; font-style: italic; font-weight: 800;
    font-size: 96px; color: var(--white); letter-spacing: -1px;
    text-shadow: 0 4px 8px rgba(0,0,0,.45);
  }
  .headline__sale {
    position: absolute; left: 182px; top: 118px;
    font-weight: 700; font-size: 82px; color: var(--yellow); letter-spacing: -1px;
    text-shadow: 0 4px 8px rgba(0,0,0,.5);
  }
  .estimate { position: absolute; right: 512px; top: 288px; text-align: right; }
  .estimate__label { font-style: italic; font-size: 22px; color: var(--white); }
  .estimate__phone { font-weight: 700; font-size: 38px; color: var(--yellow); margin-top: 2px; white-space: nowrap; }
  .offer { position: absolute; left: 223px; top: 420px; width: 340px; text-align: center; }
  .offer__price { font-weight: 900; font-size: 118px; line-height: 1; color: var(--blue); letter-spacing: -3px; }
  .offer__unit { font-style: italic; font-size: 23px; color: var(--ink); margin: -4px 0 0 110px; text-align: left; }
  .offer__product {
    font-family: "Alfa Slab One", Georgia, serif; font-size: 50px; line-height: 1.02;
    color: var(--brown-text); margin-top: 8px; text-shadow: 0 2px 3px rgba(0,0,0,.3);
  }
  .visit { position: absolute; left: 50px; top: 708px; width: 210px; text-align: center; }
  .visit__label { font-style: italic; font-size: 15px; color: var(--ink); }
  .visit__site { font-weight: 700; font-size: 19px; color: var(--ink); margin-top: 6px; }
</style>
</head>
<body>
  <main class="post">
    <svg class="post__shapes" width="790" height="790" viewBox="0 0 790 790">
      <defs>
        <radialGradient id="woodGrain" cx="50%" cy="40%" r="70%">
          <stop offset="0" stop-color="var(--wood-light)"/>
          <stop offset=".6" stop-color="var(--wood-mid)"/>
          <stop offset="1" stop-color="var(--wood-dark)"/>
        </radialGradient>
        <linearGradient id="fieldFence" x1="0" y1="0" x2="0" y2="1">
          <stop offset="0" stop-color="#6f8a4a"/>
          <stop offset=".55" stop-color="#d9c9a0"/>
          <stop offset="1" stop-color="#5d7a35"/>
        </linearGradient>
        <linearGradient id="paleFence" x1="0" y1="0" x2="0" y2="1">
          <stop offset="0" stop-color="#c7c0b2"/>
          <stop offset=".5" stop-color="#d8c49a"/>
          <stop offset="1" stop-color="#8a7a52"/>
        </linearGradient>
      </defs>
      <rect class="backdrop" width="790" height="790" fill="url(#woodGrain)" role="img" aria-label="Close-up of a cut wooden log surface with autumn leaves"/>

      <path class="brand-tab" d="M552 0H750V72L651 84L552 72Z" fill="var(--white)"/>

      <circle class="dot dot--olive" cx="57" cy="567" r="48" fill="var(--olive)"/>
      <circle class="dot dot--yellow-lg" cx="155" cy="775" r="128" fill="var(--yellow-deep)" stroke="var(--white)" stroke-width="4"/>
      <circle class="dot dot--white-lg" cx="363" cy="775" r="105" fill="var(--paper)"/>
      <circle class="dot dot--yellow-sm" cx="650" cy="795" r="75" fill="var(--yellow)"/>
      <circle class="dot dot--sky" cx="735" cy="703" r="47" fill="var(--sky)"/>

      <g class="photos" stroke="var(--white)" stroke-width="5">
        <circle cx="380" cy="310" r="86" fill="url(#fieldFence)" role="img" aria-label="Photo of a wooden picket gate set in a split rail fence"/>
        <circle cx="620" cy="382" r="103" fill="url(#paleFence)" role="img" aria-label="Photo of a new dog-ear wood privacy fence along a yard"/>
        <circle cx="170" cy="520" r="115" fill="url(#fieldFence)" role="img" aria-label="Photo of a split rail wood fence with wire mesh on a lawn"/>
        <circle cx="660" cy="615" r="105" fill="url(#paleFence)" role="img" aria-label="Photo of a wood picket fence gate with black hinges"/>
      </g>

      <circle class="offer-badge" cx="393" cy="585" r="170" fill="var(--paper)" stroke="var(--white)" stroke-width="4"/>
      <path class="chevron" d="M140 680l17 12 17-12M140 690l17 12 17-12" fill="none" stroke="var(--white)" stroke-width="2.5"/>
    </svg>

    <div class="brand">
      <span class="brand__mark"></span>
      <span class="brand__name">Oakridge Fence</span>
    </div>

    <h1 class="headline">
      <span class="headline__spring">Spring</span>
      <span class="headline__sale">Fence Sale!</span>
    </h1>

    <div class="estimate">
      <p class="estimate__label">Free Estimates</p>
      <p class="estimate__phone">555-314-2076</p>
    </div>

    <div class="offer">
      <p class="offer__price">$12</p>
      <p class="offer__unit">PER FEET</p>
      <p class="offer__product">WOOD<br>FENCES</p>
    </div>

    <div class="visit">
      <p class="visit__label">For more information, Visit:</p>
      <p class="visit__site">oakridgefenceco.com</p>
    </div>
  </main>
</body>
</html>
```